Need a pull up Banner to promote a fiction book

We need a design for a pull up banner (850mm x 2000mm) to promote a fiction book (Novel) with the author.

The book is a mystical/mythical/fantacy novel.

will attache images of the novel and the author

need the source fils in ai format

```html
<!DOCTYPE html>
<html lang="en">
<head>
<meta charset="UTF-8">
<title>The Veil of Embers – Pull-up Banner</title>
<link href="https://fonts.googleapis.com/css2?family=Cinzel:wght@400;500&family=Cormorant+Garamond:ital,wght@0,500;1,500&family=Barlow:wght@400&display=swap" rel="stylesheet">
<style>
  :root {
    --page-bg: #d3d6d9;
    --night-top: #12151d;
    --night-bottom: #1d2d4a;
    --sky-light: #e9e6df;
    --sky-warm: #d9c29a;
    --sky-cool: #8e9bab;
    --sky-deep: #4c5665;
    --title-ink: #12182a;
    --title-glint: #2a5aa8;
    --accent-blue: #3a9ad9;
    --rule-violet: #4b3f8a;
    --body-text: #f1f3f7;
  }
  * { margin: 0; padding: 0; box-sizing: border-box; }
  html, body { width: 1200px; height: 1200px; overflow: hidden; background: var(--page-bg); }
  .banner {
    position: absolute; left: 353px; top: 20px;
    width: 493px; height: 1160px;
    background: linear-gradient(180deg, var(--night-top) 40%, var(--night-bottom) 100%);
    overflow: hidden;
  }
  .hero-sky {
    position: absolute; left: 0; top: 0; width: 100%; height: 470px;
    background:
      radial-gradient(ellipse 60% 30% at 20% 55%, var(--sky-warm) 0%, transparent 70%),
      radial-gradient(ellipse 70% 25% at 50% 78%, #b9bcc2 0%, transparent 70%),
      linear-gradient(180deg, var(--sky-deep) 0%, var(--sky-cool) 25%, var(--sky-light) 50%, var(--sky-cool) 75%, var(--night-top) 100%);
  }
  .title {
    position: absolute; left: 0; top: 46px; width: 100%;
    font-family: "Cinzel", serif; font-weight: 500; text-align: center;
    color: var(--title-ink); line-height: 1;
    text-shadow: 0 0 2px rgba(42, 90, 168, .6);
  }
  .title span { display: block; }
  .title .t-the { font-size: 52px; letter-spacing: 2px; }
  .title .t-main { font-size: 92px; margin-top: 8px; letter-spacing: -1px; }
  .title .t-of { font-size: 48px; margin-top: 14px; }
  .title .t-end { font-size: 86px; margin-top: 8px; color: #15203a; }
  .subtitle {
    position: absolute; left: 0; top: 443px; width: 100%;
    font-family: "Cormorant Garamond", serif; font-weight: 500;
    font-size: 40px; text-align: center; color: var(--accent-blue);
  }
  .subtitle em { font-size: 36px; }
  .book-formats { position: absolute; left: 97px; top: 551px; width: 330px; height: 242px; }
  .author-photo { position: absolute; left: 10px; top: 800px; width: 252px; height: 360px; }
  .author-name {
    position: absolute; right: 58px; top: 843px;
    font-family: "Cormorant Garamond", serif; font-weight: 500;
    font-size: 22px; color: var(--accent-blue);
  }
  .name-rule { position: absolute; left: 238px; top: 878px; width: 200px; height: 10px; }
  .author-bio {
    position: absolute; right: 58px; top: 895px; width: 170px;
    font-family: "Barlow", sans-serif; font-size: 13.5px; line-height: 17.4px;
    text-align: right; color: var(--body-text);
  }
</style>
</head>
<body>
  <main class="banner">
    <div class="hero-sky" role="img" aria-label="Cloudy sky with a silver crown rising out of the mist"></div>

    <h1 class="title">
      <span class="t-the">THE</span>
      <span class="t-main">VEIL</span>
      <span class="t-of">OF</span>
      <span class="t-end">EMBERS</span>
    </h1>

    <p class="subtitle">A New Age <em>of</em> Velmoria</p>

    <svg class="book-formats" viewBox="0 0 330 242" role="img" aria-label="Book shown as paperback, tablet and phone editions">
      <defs>
        <linearGradient id="coverTone" x1="0" y1="0" x2="0" y2="1">
          <stop offset="0" stop-color="#8e9bab"/>
          <stop offset=".45" stop-color="#d6d3cc"/>
          <stop offset=".7" stop-color="#5b6372"/>
          <stop offset="1" stop-color="#141a2a"/>
        </linearGradient>
      </defs>
      <rect x="0" y="37" width="142" height="198" rx="8" fill="#0c0d10"/>
      <rect x="14" y="50" width="114" height="172" fill="url(#coverTone)"/>
      <rect x="137" y="0" width="158" height="238" fill="url(#coverTone)"/>
      <rect x="295" y="4" width="8" height="234" fill="#c9c6bd"/>
      <rect x="87" y="103" width="76" height="138" rx="9" fill="#0c0d10"/>
      <rect x="92" y="114" width="66" height="114" fill="url(#coverTone)"/>
    </svg>

    <svg class="author-photo" viewBox="0 0 252 360" role="img" aria-label="Portrait photo of the author">
      <path d="M70 360 L60 200 Q80 150 126 140 Q172 150 192 200 L185 360 Z" fill="#0d0f14"/>
      <ellipse cx="126" cy="90" rx="55" ry="75" fill="#1a1614"/>
    </svg>

    <h2 class="author-name">Mira Calden Oyelaran</h2>
    <svg class="name-rule" viewBox="0 0 200 10" aria-hidden="true">
      <line x1="4" y1="5" x2="196" y2="5" stroke="var(--rule-violet)" stroke-width="1.5"/>
      <path d="M0 5 L4 1 L8 5 L4 9 Z M192 5 L196 1 L200 5 L196 9 Z" fill="var(--rule-violet)"/>
    </svg>
    <p class="author-bio">Lorem ipsum dolor sit amet, consectetur adipiscing elit, sed do eiusmod tempor incididunt ut labore et dolore magna aliqua. Quis ipsum suspendisse ultrices gravida. Risus commodo viverra maecenas accumsan</p>
  </main>
</body>
</html>
```